Harbor Yield Group brochure

I need a standard 8 1/2 x 11 brochure and it must have a place for addresses and a stamp to mail located on the back (meet US postal requirements). I have logo and copy but will need a few unique images/icons to make it look great. I am a start up business development company that specializes in lead generation, blogging, social media, etc. Brochure must stand out in the mail and have that wow factor but must be clean as well. I would also like the topics provided to not stay within the lines of the folds on the brochure. Would like it to be free flowing without boundaries.

Please do no include the wine logo

Industry/Entity Type

Group

```html
<!DOCTYPE html>
<html lang="en">
<head>
<meta charset="utf-8">
<title>Harbor Yield Group – Brochure Presentation</title>
<link href="https://fonts.googleapis.com/css2?family=Tinos:ital,wght@0,400;0,700;1,400;1,700&family=Arimo:wght@400&display=swap" rel="stylesheet">
<style>
  :root{
    --board:#000000;
    --paper:#ffffff;
    --ink:#1e1e1e;
    --green-dark:#4f8a1f;
    --green:#7db83a;
    --green-mid:#a9d26a;
    --green-light:#dcecb4;
    --green-pale:#f1f7e0;
    --label:#cfcfcf;
    --photo-skin:#b58d74;
    --photo-office:#8a8f93;
  }
  *{box-sizing:border-box;margin:0;padding:0}
  html,body{width:1200px;height:1002px;overflow:hidden;background:var(--board)}
  body{position:relative;font-family:"Tinos","Times New Roman",serif;color:var(--ink)}

  .board-label{position:absolute;font-family:"Arimo",Arial,sans-serif;font-size:12px;color:var(--label)}

  /* ---------- outside spread ---------- */
  .outside{position:absolute;left:88px;top:40px;width:640px;height:427px;display:flex;background:var(--paper)}
  .panel{position:relative;height:100%;overflow:hidden}
  .panel--story{width:200px;padding:14px 12px 0 14px;font-size:8.2px;line-height:1.25}
  .panel--mailer{width:166px;background:var(--paper);border-left:1px dashed #d6d6d6;border-right:1px dashed #d6d6d6}

  .story-title{font-weight:700;font-size:12.5px;text-align:center}
  .story-sub{font-weight:700;font-style:italic;font-size:9.5px;text-align:center;margin-bottom:3px}
  .story p{text-indent:10px;text-align:justify}
  .story-heading{font-weight:700;font-size:11.5px;text-align:center;margin:6px 0 3px}
  .story-list{list-style:none}
  .story-list li{position:relative;padding-left:14px;margin-bottom:4px;text-align:justify}
  .story-list li::before,.fact-list li::before,.lead-list li::before{content:"";position:absolute;left:0;top:1px;width:9px;height:9px;border-radius:50%;background:var(--green)}
  .story-photo{position:absolute;left:0;bottom:0;width:100%;height:78px;background:linear-gradient(120deg,#6b5a48 0%,#9c8a74 45%,#c9d23d 80%,#3d3a36 100%)}

  .stamp-box{position:absolute;left:14px;top:20px;width:44px;height:36px;border:1px solid #9a9a9a;background:#f4f4f4}
  .address-card{position:absolute;left:70px;top:20px;width:84px;height:318px;border:1px solid #e2e2e2;border-radius:14px;background:#fcfcfc}
  .return-address{position:absolute;left:8px;top:330px;transform-origin:left top;transform:rotate(-90deg);width:300px;white-space:nowrap}
  .return-address .brand-name{font-size:17px}
  .return-address .addr{font-size:6.5px;line-height:1.2;margin-top:2px}
  .mailer-wave{position:absolute;left:0;bottom:0;width:100%;height:80px}

  /* ---------- front panel (shared) ---------- */
  .front{position:relative;overflow:hidden;background:linear-gradient(180deg,var(--green-light) 0%,var(--green-pale) 22%,var(--paper) 40%)}
  .front-head{position:relative;padding:0.6em 0.7em 0}
  .front-title{color:var(--green-dark);font-weight:700;font-size:1.55em;line-height:1.02}
  .front-sub{font-style:italic;font-weight:700;font-size:0.82em;line-height:1.15;margin-top:0.2em}
  .front-dot{position:absolute;right:1.1em;top:0.7em;width:1.5em;height:1.5em;border-radius:50%;background:var(--green)}
  .front-photo{position:absolute;left:0;width:100%;background:linear-gradient(160deg,var(--photo-office) 0%,#c9c4bd 35%,var(--photo-skin) 55%,#5b4a3f 80%,#8b7161 100%)}
  .front-wave{position:absolute;left:0;bottom:0;width:100%}
  .front-foot{position:absolute;left:0;bottom:0;width:100%;text-align:center}
  .brand-name{font-family:"Tinos","Times New Roman",serif;font-weight:700;color:var(--ink);letter-spacing:0.01em}
  .front-foot .brand-name{font-size:1.3em}
  .front-tag{font-style:italic;font-weight:700;font-size:0.8em;line-height:1.15;margin-top:0.35em}
  .front-phone{color:var(--green-dark);font-weight:700;font-size:1.25em;margin:0.2em 0 0.5em}

  .panel--front{width:274px;font-size:13px}
  .panel--front .front-photo{top:86px;height:222px}
  .panel--front .front-wave{height:150px}

  .front-single{position:absolute;left:883px;top:280px;width:192px;height:416px;font-size:10.5px}
  .front-single .front-photo{top:76px;height:200px}
  .front-single .front-wave{height:160px}

  /* ---------- inside spread ---------- */
  .inside{position:absolute;left:277px;top:509px;width:608px;height:432px;background:var(--paper);overflow:hidden;font-size:7.2px;line-height:1.2}
  .inside-photo{position:absolute;left:0;top:0;width:240px;height:370px;background:linear-gradient(150deg,#c89a5a 0%,#e2d3b7 30%,#7fa8c2 55%,#c5a286 70%,#efefef 100%)}
  .inside-wave{position:absolute;left:0;bottom:0;width:100%;height:150px}
  .inside-col{position:absolute;top:8px;width:180px;text-align:justify}
  .inside-col--blog{left:242px;width:178px}
  .inside-col--leads{left:424px;width:178px}
  .col-title{font-weight:700;font-size:9.6px;color:var(--ink)}
  .col-title--green{color:var(--green-dark)}
  .col-sub{font-weight:700;font-style:italic;font-size:8px}
  .inside p{text-indent:8px}
  .fact-list,.lead-list,.step-list{list-style:none;margin:3px 0}
  .fact-list li,.lead-list li{position:relative;padding-left:13px;margin-bottom:4px}
  .step-list li{position:relative;padding-left:13px;margin-bottom:5px;counter-increment:step}
  .step-list{counter-reset:step}
  .step-list li::before{content:counter(step);position:absolute;left:0;top:0;width:9px;height:9px;border-radius:50%;background:var(--green-dark);color:#fff;font-size:6px;text-align:center;line-height:9px}
  .money{font-weight:700;font-size:8.2px;margin-top:5px}
  .specialties{list-style:none;padding-left:12px}
  .inside-foot{position:absolute;left:0;bottom:12px;width:100%;text-align:center}
  .inside-foot .brand-name{font-size:20px;display:block;margin-left:-60px}
  .inside-foot .front-tag{font-size:9px;margin-left:150px}
</style>
</head>
<body>

<!-- Outside spread -->
<section class="outside">
  <div class="panel panel--story story">
    <h2 class="story-title">Strategic Brand Positioning:</h2>
    <p class="story-sub">It's all about the Experience!</p>
    <p>Great brands always start with a plan and nothing matters more to your business than your perceived value to potential customers.</p>
    <p>As you know, there are many other competitors in your niche. The process of becoming #1 can be extremely complicated because quite frankly every business niche is unique.</p>
    <p>Harbor Yield Group will position your business as the most recognized brand in your niche and <b><i>THE ONLY LOGICAL CHOICE!</i></b></p>
    <h3 class="story-heading">How We Make This Happen:</h3>
    <ul class="story-list">
      <li>Logos, color schemes and fonts play an important role in brand position but the most important piece is separating your brand from the rest to experience potential customers associate your company with. This is the hardest part when creating a unique and recognizable brand.</li>
      <li>Create a unique action plan that includes marketing, community involvement, increased website traffic, press releases and modifying your content public relations plan.</li>
      <li>After you become the only logical choice in your niche, the last step is keeping your business #1. The creation of a master strategic plan will allow you to keep top of mind awareness for years to come.</li>
    </ul>
    <div class="story-photo" role="img" aria-label="Photo of a hand holding a tablet outdoors"></div>
  </div>

  <div class="panel panel--mailer">
    <div class="stamp-box" aria-label="Stamp area"></div>
    <div class="address-card" aria-label="Mailing address area"></div>
    <div class="return-address">
      <div class="brand-name">Harbor Yield Group, LLC.</div>
      <div class="addr">Harbor Yield Group, LLC<br>1200 Harbor Way, Suite 4<br>Spokane, WA 99201</div>
    </div>
    <svg class="mailer-wave" viewBox="0 0 166 80" preserveAspectRatio="none" aria-hidden="true">
      <path d="M0 30 C40 10 100 50 166 22 L166 80 L0 80 Z" fill="var(--green-light)"/>
      <path d="M0 50 C50 30 110 70 166 44 L166 80 L0 80 Z" fill="var(--green-mid)"/>
    </svg>
  </div>

  <div class="panel panel--front front">
    <div class="front-head">
      <h1 class="front-title">Dominate Your<br>Competition!</h1>
      <p class="front-sub">Become the Only Logical Choice<br>in Your Business Niche!</p>
      <span class="front-dot"></span>
    </div>
    <div class="front-photo" role="img" aria-label="Photo of a businesswoman with glasses seated at a computer"></div>
    <svg class="front-wave" viewBox="0 0 274 150" preserveAspectRatio="none" aria-hidden="true">
      <path d="M0 40 C80 0 170 70 274 20 L274 150 L0 150 Z" fill="var(--green-mid)"/>
      <path d="M0 58 C90 28 180 80 274 40 L274 150 L0 150 Z" fill="var(--green-light)"/>
      <path d="M0 120 C90 100 190 140 274 110 L274 150 L0 150 Z" fill="var(--green-mid)"/>
    </svg>
    <div class="front-foot">
      <div class="brand-name">Harbor Yield Group, LLC.</div>
      <p class="front-tag">Master Marketing Strategists<br>Focused on Increasing Your Profits<br>and Building Your Legacy.</p>
      <p class="front-phone">509-555-0148</p>
    </div>
  </div>
</section>
<span class="board-label" style="left:739px;top:452px">Outside</span>

<!-- Front panel -->
<section class="front front-single">
  <div class="front-head">
    <h1 class="front-title">Dominate Your<br>Competition!</h1>
    <p class="front-sub">Become the Only Logical Choice<br>in Your Business Niche!</p>
    <span class="front-dot"></span>
  </div>
  <div class="front-photo" role="img" aria-label="Photo of a businesswoman with glasses seated at a computer"></div>
  <svg class="front-wave" viewBox="0 0 192 160" preserveAspectRatio="none" aria-hidden="true">
    <path d="M0 40 C60 0 120 70 192 20 L192 160 L0 160 Z" fill="var(--green-mid)"/>
    <path d="M0 58 C64 28 130 80 192 40 L192 160 L0 160 Z" fill="var(--green-light)"/>
    <path d="M0 130 C64 110 130 150 192 120 L192 160 L0 160 Z" fill="var(--green-mid)"/>
  </svg>
  <div class="front-foot">
    <div class="brand-name">Harbor Yield Group, LLC.</div>
    <p class="front-tag">Master Marketing Strategists<br>Focused on Increasing Your Profits<br>and Building Your Legacy.</p>
    <p class="front-phone">509-555-0148</p>
  </div>
</section>
<span class="board-label" style="left:957px;top:711px">Front Panel</span>

<!-- Inside spread -->
<section class="inside">
  <div class="inside-photo" role="img" aria-label="Photo of a smiling man wearing a headset, writing at a desk"></div>
  <svg class="inside-wave" viewBox="0 0 608 150" preserveAspectRatio="none" aria-hidden="true">
    <path d="M0 30 C160 -10 330 80 608 20 L608 150 L0 150 Z" fill="var(--green-light)"/>
    <path d="M0 60 C180 20 360 100 608 50 L608 150 L0 150 Z" fill="var(--green-mid)"/>
    <path d="M0 80 C200 50 380 120 608 80 L608 150 L0 150 Z" fill="var(--green-light)"/>
  </svg>

  <div class="inside-col inside-col--blog">
    <h2 class="col-title">Blogging to Generate Revenue:</h2>
    <p class="col-sub">Not just for Nerds, Hipsters and Techies!</p>
    <p>Blogging has become so powerful if you are not blogging your company is falling in Searchly Search rankings (SEO). A recent study suggests businesses in the top 3 Searchly rankings generate 61.5% of the traffic. More website traffic paired with compelling online marketing content leads to more sales.</p>
    <h3 class="col-title col-title--green">Unique Blogging Facts:</h3>
    <ul class="fact-list">
      <li>77% of internet users read blogs</li>
      <li>57% of companies with a blog have acquired a customer from their blog</li>
      <li>61% of US consumers have made a purchase based on blog</li>
      <li>Websites with blogs have 434% more indexed pages</li>
      <li>And most importantly.... Small businesses with blogs generate 126% more leads!</li>
    </ul>
    <p class="money">We help you turn a blog into a MONEY MAKING MACHINE for your business:</p>
    <p>We will teach you the correct way to blog and how to avoid some of the Blogging Blunders.</p>
    <ol class="step-list">
      <li>Spending too much time setting up a blog</li>
      <li>Not knowing your audience</li>
      <li>Having "NO Call to Action"</li>
      <li>Lack of compelling engaging content</li>
    </ol>
  </div>

  <div class="inside-col inside-col--leads">
    <h2 class="col-title">Lead Generation and Conversion:</h2>
    <p class="col-sub">Just like speed dating.... Well maybe not!</p>
    <p>Ever wondered why a few businesses seem like they have so many leads they have to turn business away? It's simple, they generate a massive amount of leads.</p>
    <p>Customers don't buy from every business they come into contact with so having tons of leads in your pipeline will make your business very profitable. You're not a rocket scientist and neither are we, but we both know more leads translate into more sales!</p>
    <h3 class="col-title col-title--green">Generate More Leads by:</h3>
    <ul class="lead-list">
      <li>Capturing more emails and creating special offers for potential customers</li>
      <li>Using social media sites</li>
      <li>Creating compelling email offers to your current database – <i>businesses typically don't understand how to make money from their current customers.</i></li>
      <li>Using your website and blog</li>
      <li>Using direct mail and other traditional marketing efforts which you are easily able to track results and see the impact of motivating offers.</li>
    </ul>
    <h3 class="col-title col-title--green">Our Other Specialties:</h3>
    <ul class="specialties">
      <li>Website Design &amp; Creation</li>
      <li>Traditional Marketing Methods</li>
      <li>Public Relations</li>
      <li>SEO (Search Engine Optimization)</li>
      <li>Event Management</li>
      <li>Database/Email marketing</li>
    </ul>
  </div>

  <div class="inside-foot">
    <span class="brand-name">Harbor Yield Group, LLC.</span>
    <p class="front-tag">Master Marketing Strategists Focused on Increasing<br>YOUR Profits and Building YOUR Legacy.</p>
  </div>
</section>
<span class="board-label" style="left:864px;top:924px">Inside</span>

</body>
</html>
```